Business card design needed

A mobile coffee, eats and treats van. We sell freshly ground Morlandi coffee, a selection of yummy things to eats, and lovely giftwares, including candles, scarfs, jewellery. We also have an online store where additional home and giftwares can be purchased
Updates

Thanks so much for all your efforts so far, I have received some great concepts.  Just wanted to send out a reminder that our concept is coffee, eats and treats (the treats being home and gift ware)  We have a mobile van and also an online store.  I dont want to make my business card too "busy" but at the same time I would like to give my potential customers something that will really excite and intrigue them...

Thank you everyone for your designs...I think I have made a decision...have just sent out a couple of questions.  I will be loading a new project shortly if you are interested?  Thanks, Helena

Industry/Entity Type

Store

Contact Information for Business Card

The Little Sparrow - Coffee, Eats & Treats
Helena Marquardt
0439 582 616
helena@thelittlesparrow.com.au
www.thelittlesparrow.com.au
www.facebook.com/thelittlesparrow
https://twitter.com/TheLittleSparrow

Requirements
Nice to have
• It would be good to have a rewards program on the back, we can tick off when prople buy coffee....5th coffee free...something like that...

It would also be good for the card to look like a gift tag....

```html
<!DOCTYPE html>
<html lang="en">
<head>
<meta charset="utf-8">
<title>The Little Sparrow – Business Card</title>
<link rel="stylesheet" href="https://fonts.googleapis.com/css2?family=Crimson+Text:wght@400;600&display=swap">
<style>
  :root {
    --backdrop: #ddd8cc;
    --card-cream: #f5f6e9;
    --card-olive: #b9b46b;
    --ink: #1d1b12;
    --brand-olive: #9d9652;
    --icon-dark: #2b2a20;
    --icon-soft: #7d7844;
  }
  * { box-sizing: border-box; margin: 0; padding: 0; }
  html, body {
    width: 1200px;
    height: 800px;
    overflow: hidden;
    background: var(--backdrop);
  }
  body {
    display: flex;
    align-items: center;
    justify-content: center;
    font-family: "Crimson Text", Georgia, serif;
    color: var(--ink);
  }
  .business-card {
    width: 900px;
    height: 514px;
    display: flex;
    box-shadow: 0 10px 28px rgba(0, 0, 0, 0.25);
  }
  .brand-panel {
    width: 362px;
    background: var(--card-cream);
    display: flex;
    align-items: center;
    justify-content: center;
    gap: 12px;
    padding-bottom: 30px;
  }
  .brand-dot {
    width: 14px;
    height: 14px;
    border-radius: 50%;
    background: var(--brand-olive);
    flex-shrink: 0;
  }
  .brand-name {
    font-size: 34px;
    font-weight: 600;
    color: var(--brand-olive);
    letter-spacing: 0.2px;
    white-space: nowrap;
  }
  .details-panel {
    flex: 1;
    background: var(--card-olive);
    padding: 122px 0 0 40px;
  }
  .person-name {
    font-size: 33px;
    font-weight: 600;
    line-height: 1.1;
  }
  .person-role {
    font-size: 23px;
    font-weight: 600;
    margin: 10px 0 0 10px;
  }
  .contact-list {
    list-style: none;
    margin-top: 66px;
  }
  .contact-item {
    display: flex;
    align-items: center;
    height: 36px;
    font-size: 19px;
    white-space: nowrap;
  }
  .contact-icon {
    width: 26px;
    height: 26px;
    margin-right: 30px;
    display: flex;
    align-items: center;
    justify-content: center;
    flex-shrink: 0;
  }
  .contact-icon--at {
    font-size: 24px;
    font-weight: 600;
    color: var(--icon-dark);
  }
  .contact-icon--plain span {
    display: block;
    width: 22px;
    height: 22px;
    border-radius: 4px;
    background: var(--icon-soft);
  }
  .contact-icon--round span {
    display: block;
    width: 22px;
    height: 22px;
    border-radius: 50%;
    background: var(--icon-soft);
  }
</style>
</head>
<body>
  <article class="business-card">
    <section class="brand-panel">
      <span class="brand-dot"></span>
      <span class="brand-name">The Little Sparrow</span>
    </section>
    <section class="details-panel">
      <h1 class="person-name">Helena Marquardt</h1>
      <p class="person-role">Business Partner</p>
      <ul class="contact-list">
        <li class="contact-item">
          <span class="contact-icon">
            <svg width="26" height="24" viewBox="0 0 26 24" aria-hidden="true">
              <path d="M2 7 Q13 0 24 7 L24 10 L19 10 L19 7 Q13 5 7 7 L7 10 L2 10 Z" fill="var(--icon-dark)"/>
              <path d="M6 12 L20 12 L23 22 L3 22 Z" fill="var(--icon-dark)"/>
              <circle cx="13" cy="17" r="3" fill="var(--card-olive)"/>
            </svg>
          </span>
          T.p: 0439 582 616
        </li>
        <li class="contact-item">
          <span class="contact-icon contact-icon--round"><span></span></span>
          www.thelittlesparrow.com.au
        </li>
        <li class="contact-item">
          <span class="contact-icon contact-icon--at">@</span>
          helena@thelittlesparrow.com.au
        </li>
        <li class="contact-item">
          <span class="contact-icon contact-icon--plain"><span></span></span>
          www.friendhub.com/thelittlesparrow
        </li>
        <li class="contact-item">
          <span class="contact-icon contact-icon--plain"><span></span></span>
          https://chirpline.com/TheLittleSparrow
        </li>
      </ul>
    </section>
  </article>
</body>
</html>
```